Redesign of iOS App Lumo Tutor

Redesign of existing App Lumo Tutor, an app that helps learning Japanese Kanjis, Hiragana, Katakana.

The functionallity should remain the same as today: the app is free, you may download it at the app store. But: I like the design of my other apps better ;)

Target Market(s)

Students learning Japanese

Industry/Entity Type

Teacher

Font styles to use
Sans Serif

Requirements
Must have
• Lumo Tutor has 7 main screens, all screens has to be designed for iPhone and iPad: Main, Settings, Reading Tests, Writing Tests, Game, Paper Mode, Search
Nice to have
• I like the logo as it is today

```html
<!DOCTYPE html>
<html lang="en">
<head>
<meta charset="utf-8">
<title>Lumo Tutor – N5 Statistics</title>
<link rel="stylesheet" href="https://fonts.googleapis.com/css2?family=Roboto:wght@400;500;700&display=swap">
<style>
  :root {
    --bg: #ffffff;
    --status-bg: #f7f7f7;
    --ink: #111111;
    --card: #ffffff;
    --dot-test: #a3a3a3;
    --dot-correct: #13c2ad;
    --dot-score: #439ff5;
    --dot-wrong: #f25d49;
    --accent: #c0192f;
    --cell-1: #f7e3e5;
    --cell-2: #f7dadd;
    --cell-3: #e9cdd0;
    --cell-4: #efd9da;
    --cell-5: #efd1d4;
    --cell-6: #e2c9cc;
  }
  * { box-sizing: border-box; margin: 0; padding: 0; }
  html, body { width: 675px; height: 1200px; overflow: hidden; }
  body {
    background: var(--bg);
    font-family: "Roboto", sans-serif;
    color: var(--ink);
    position: relative;
  }
  .status-bar {
    position: absolute; left: 0; top: 0; width: 675px; height: 36px;
    background: var(--status-bg);
    font-size: 18px; font-weight: 500;
    display: flex; align-items: center; justify-content: space-between;
    padding: 0 8px 0 10px;
  }
  .status-left, .status-right { display: flex; align-items: center; gap: 8px; width: 200px; }
  .status-right { justify-content: flex-end; gap: 6px; }
  .status-time { position: absolute; left: 0; right: 0; text-align: center; pointer-events: none; }

  .tabs {
    position: absolute; left: 41px; top: 990px; width: 594px; height: 93px;
    display: flex; gap: 1.5px;
  }
  .tab {
    flex: 1; background: var(--card);
    border-radius: 0 0 9px 9px;
    box-shadow: 0 2px 5px rgba(0,0,0,0.18);
    display: flex; align-items: center; justify-content: center;
    padding-top: 18px;
    font-size: 24px; font-weight: 700;
  }
  .tab.active { background: var(--accent); color: #fff; }
  .tab-notch { position: absolute; left: 157px; top: 976px; }

  .stats-card {
    position: absolute; left: 41px; top: 86px; width: 594px; height: 915px;
    background: var(--card); border-radius: 9px;
    box-shadow: 0 2px 8px rgba(0,0,0,0.22);
    padding: 0 22px;
  }
  .legend {
    height: 56px; display: flex; align-items: center;
    font-size: 20px; position: relative;
  }
  .legend-item { position: absolute; display: flex; align-items: center; gap: 16px; }
  .dot { width: 18px; height: 18px; border-radius: 50%; display: inline-block; flex: none; }
  .dot.test { background: var(--dot-test); }
  .dot.correct { background: var(--dot-correct); }
  .dot.score { background: var(--dot-score); }
  .dot.wrong { background: var(--dot-wrong); }

  .test-grid {
    display: grid; grid-template-columns: 270px 270px; grid-auto-rows: 160px;
    gap: 5px 5px;
  }
  .test-cell { position: relative; font-size: 20px; }
  .test-title {
    position: absolute; top: 22px; left: 0; right: 0;
    display: flex; justify-content: center; align-items: center; gap: 8px;
  }
  .stat { position: absolute; display: flex; align-items: center; gap: 16px; }
  .stat.r1 { top: 85px; } .stat.r2 { top: 125px; }
  .stat.c1 { left: 24px; } .stat.c2 { left: 161px; }

  .bottom-nav {
    position: absolute; left: 0; top: 1126px; width: 675px; height: 34px;
    font-size: 25px; font-weight: 700;
  }
  .nav-item { position: absolute; transform: translateX(-50%); }
</style>
</head>
<body>
  <header class="status-bar">
    <div class="status-left">
      <svg width="62" height="10" viewBox="0 0 62 10" aria-hidden="true">
        <g fill="#111"><circle cx="5" cy="5" r="4.5"/><circle cx="17" cy="5" r="4.5"/><circle cx="29" cy="5" r="4.5"/><circle cx="41" cy="5" r="4.5"/><circle cx="53" cy="5" r="4.5"/></g>
      </svg>
      <svg width="20" height="15" viewBox="0 0 20 15" aria-hidden="true">
        <path d="M10 14 L6.5 10.3 A5 5 0 0 1 13.5 10.3 Z" fill="#111"/>
        <path d="M3.5 7.5 A9 9 0 0 1 16.5 7.5" stroke="#111" stroke-width="2" fill="none"/>
        <path d="M0.8 4.6 A13 13 0 0 1 19.2 4.6" stroke="#111" stroke-width="2" fill="none"/>
      </svg>
    </div>
    <div class="status-time">9:41 AM</div>
    <div class="status-right">
      <span>100%</span>
      <svg width="40" height="18" viewBox="0 0 40 18" aria-hidden="true">
        <rect x="0.75" y="0.75" width="34" height="16.5" rx="3" fill="none" stroke="#111" stroke-width="1.5"/>
        <rect x="3" y="3" width="29.5" height="12" rx="1.5" fill="#111"/>
        <rect x="36.5" y="6" width="2.5" height="6" rx="1" fill="#111"/>
      </svg>
    </div>
  </header>

  <nav class="tabs">
    <div class="tab">K</div>
    <div class="tab active">N5</div>
    <div class="tab">N4</div>
    <div class="tab">N3</div>
    <div class="tab">N2</div>
    <div class="tab">N1</div>
    <div class="tab">
      <svg width="26" height="25" viewBox="0 0 24 23" aria-label="Favourites"><path d="M12 0.5 L15 8 L23 8.4 L16.8 13.5 L18.9 21.5 L12 17 L5.1 21.5 L7.2 13.5 L1 8.4 L9 8 Z" fill="#111"/></svg>
    </div>
  </nav>
  <svg class="tab-notch" width="24" height="14" viewBox="0 0 24 14" aria-hidden="true">
    <path d="M0 14 Q6 14 9 5 Q12 -2 15 5 Q18 14 24 14 Z" fill="var(--accent)"/>
  </svg>

  <main class="stats-card">
    <div class="legend">
      <span class="legend-item" style="left:9px"><i class="dot test"></i>Test</span>
      <span class="legend-item" style="left:165px"><i class="dot correct"></i>Correct</span>
      <span class="legend-item" style="left:322px"><i class="dot score"></i>Score</span>
      <span class="legend-item" style="left:470px"><i class="dot wrong"></i>Wrong</span>
    </div>

    <section class="test-grid">
      <article class="test-cell" style="background:var(--cell-1)">
        <h2 class="test-title" style="font-weight:400;font-size:20px">Kanji <svg width="34" height="18" viewBox="0 0 34 18"><path d="M1 9 H31 M23 1.5 L31.5 9 L23 16.5" stroke="#111" stroke-width="2.4" fill="none"/></svg> Meaning</h2>
        <div class="stat r1 c1"><i class="dot test"></i>103</div><div class="stat r1 c2"><i class="dot correct"></i>0</div>
        <div class="stat r2 c1"><i class="dot score"></i>0</div><div class="stat r2 c2"><i class="dot wrong"></i>0</div>
      </article>
      <article class="test-cell" style="background:var(--cell-2)">
        <h2 class="test-title" style="font-weight:400;font-size:20px">Meaning <svg width="34" height="18" viewBox="0 0 34 18"><path d="M1 9 H31 M23 1.5 L31.5 9 L23 16.5" stroke="#111" stroke-width="2.4" fill="none"/></svg> Kanji</h2>
        <div class="stat r1 c1"><i class="dot test"></i>103</div><div class="stat r1 c2"><i class="dot correct"></i>0</div>
        <div class="stat r2 c1"><i class="dot score"></i>0</div><div class="stat r2 c2"><i class="dot wrong"></i>0</div>
      </article>
      <article class="test-cell" style="background:var(--cell-3)">
        <h2 class="test-title" style="font-weight:400;font-size:20px">Kanji <svg width="34" height="18" viewBox="0 0 34 18"><path d="M1 9 H31 M23 1.5 L31.5 9 L23 16.5" stroke="#111" stroke-width="2.4" fill="none"/></svg> On</h2>
        <div class="stat r1 c1"><i class="dot test"></i>103</div><div class="stat r1 c2"><i class="dot correct"></i>0</div>
        <div class="stat r2 c1"><i class="dot score"></i>0</div><div class="stat r2 c2"><i class="dot wrong"></i>0</div>
      </article>
      <article class="test-cell" style="background:var(--cell-4)">
        <h2 class="test-title" style="font-weight:400;font-size:20px">On <svg width="34" height="18" viewBox="0 0 34 18"><path d="M1 9 H31 M23 1.5 L31.5 9 L23 16.5" stroke="#111" stroke-width="2.4" fill="none"/></svg> Kanji</h2>
        <div class="stat r1 c1"><i class="dot test"></i>103</div><div class="stat r1 c2"><i class="dot correct"></i>0</div>
        <div class="stat r2 c1"><i class="dot score"></i>0</div><div class="stat r2 c2"><i class="dot wrong"></i>0</div>
      </article>
      <article class="test-cell" style="background:var(--cell-5)">
        <h2 class="test-title" style="font-weight:400;font-size:20px">Kanji <svg width="34" height="18" viewBox="0 0 34 18"><path d="M1 9 H31 M23 1.5 L31.5 9 L23 16.5" stroke="#111" stroke-width="2.4" fill="none"/></svg> Kun</h2>
        <div class="stat r1 c1"><i class="dot test"></i>103</div><div class="stat r1 c2"><i class="dot correct"></i>0</div>
        <div class="stat r2 c1"><i class="dot score"></i>0</div><div class="stat r2 c2"><i class="dot wrong"></i>0</div>
      </article>
      <article class="test-cell" style="background:var(--cell-6)">
        <h2 class="test-title" style="font-weight:400;font-size:20px">Kun <svg width="34" height="18" viewBox="0 0 34 18"><path d="M1 9 H31 M23 1.5 L31.5 9 L23 16.5" stroke="#111" stroke-width="2.4" fill="none"/></svg> Kanji</h2>
        <div class="stat r1 c1"><i class="dot test"></i>103</div><div class="stat r1 c2"><i class="dot correct"></i>0</div>
        <div class="stat r2 c1"><i class="dot score"></i>0</div><div class="stat r2 c2"><i class="dot wrong"></i>0</div>
      </article>
      <article class="test-cell" style="background:var(--cell-6)">
        <h2 class="test-title" style="font-weight:400;font-size:20px">Word <svg width="34" height="18" viewBox="0 0 34 18"><path d="M1 9 H31 M23 1.5 L31.5 9 L23 16.5" stroke="#111" stroke-width="2.4" fill="none"/></svg> Reading</h2>
        <div class="stat r1 c1"><i class="dot test"></i>103</div><div class="stat r1 c2"><i class="dot correct"></i>0</div>
        <div class="stat r2 c1"><i class="dot score"></i>0</div><div class="stat r2 c2"><i class="dot wrong"></i>0</div>
      </article>
      <article class="test-cell" style="background:var(--cell-4)">
        <h2 class="test-title" style="font-weight:400;font-size:20px">Reading <svg width="34" height="18" viewBox="0 0 34 18"><path d="M1 9 H31 M23 1.5 L31.5 9 L23 16.5" stroke="#111" stroke-width="2.4" fill="none"/></svg> Word</h2>
        <div class="stat r1 c1"><i class="dot test"></i>103</div><div class="stat r1 c2"><i class="dot correct"></i>0</div>
        <div class="stat r2 c1"><i class="dot score"></i>0</div><div class="stat r2 c2"><i class="dot wrong"></i>0</div>
      </article>
      <article class="test-cell" style="background:var(--cell-5)">
        <h2 class="test-title" style="font-weight:400;font-size:20px">Writing</h2>
        <div class="stat r1 c1"><i class="dot test"></i>103</div><div class="stat r1 c2"><i class="dot correct"></i>0</div>
        <div class="stat r2 c1"><i class="dot score"></i>0</div><div class="stat r2 c2"><i class="dot wrong"></i>0</div>
      </article>
      <article class="test-cell" style="background:var(--cell-1)">
        <h2 class="test-title" style="font-weight:400;font-size:20px">All Tests</h2>
        <div class="stat r1 c1"><i class="dot test"></i>103</div><div class="stat r1 c2"><i class="dot correct"></i>0</div>
        <div class="stat r2 c1"><i class="dot score"></i>0</div><div class="stat r2 c2"><i class="dot wrong"></i>0</div>
      </article>
    </section>
  </main>

  <nav class="bottom-nav">
    <span class="nav-item" style="left:114px">Game</span>
    <span class="nav-item" style="left:263px">Paper</span>
    <span class="nav-item" style="left:411px">Search</span>
    <span class="nav-item" style="left:560px">Setting</span>
  </nav>
</body>
</html>
```